MOBILE DOG GROOMING BUSINESS CARD

We need a business card for a new local Mobile Dog groomer wanting to attract new business.

Our logo must be incorporated on the first page with contact details on the front or back of the card. We were thinking for the back of the card it could have the " your next appointment is on date...time...

Target Market(s)

local pet lovers and owners

Industry/Entity Type

Business

Contact Information for Business Card

Maren Tolley
Certified Professional Groomer
0437825190
www.pawluxemobilewash.com.au
pawluxemobilewash@quillmail.com

Font styles to use
Script

Colors

Designer to choose colors to be used in the design.

Requirements
Must have
• Must have our logo on the front
Possibly something that says like our page and check us out on facebook
Nice to have
• Colours are something we would like - matched in with the logo.
Should not have
• Clutter

```html
<!DOCTYPE html>
<html lang="en">
<head>
<meta charset="utf-8">
<title>Next Appointment Card</title>
<link rel="stylesheet" href="https://fonts.googleapis.com/css2?family=Archivo:wght@400&display=swap">
<style>
  :root {
    --paper: #ffffff;
    --heading-grey: #858585;
    --rose: #d07091;
    --web-grey: #b8b8b8;
    --ink-navy: #1c1a45;
  }
  html, body {
    margin: 0;
    padding: 0;
    width: 1200px;
    height: 707px;
    overflow: hidden;
    background: var(--paper);
  }
  .appointment-card {
    position: relative;
    width: 1200px;
    height: 707px;
    background: var(--paper);
    font-family: "Archivo", "Helvetica Neue", Arial, sans-serif;
  }
  .card-heading {
    position: absolute;
    left: 40px;
    top: 12px;
    margin: 0;
    font-weight: 400;
    font-size: 67px;
    letter-spacing: 3px;
    color: var(--heading-grey);
  }
  .entry-field {
    position: absolute;
    display: flex;
    align-items: flex-end;
    color: var(--rose);
    font-size: 65px;
    letter-spacing: 3px;
  }
  .entry-field .field-label { line-height: 1; }
  .entry-field .field-line {
    height: 4px;
    background: var(--rose);
    margin-left: 4px;
    margin-bottom: 3px;
  }
  .entry-date { left: 68px; top: 200px; }
  .entry-date .field-line { width: 935px; }
  .entry-time { left: 74px; top: 369px; }
  .entry-time .field-line { width: 938px; }
  .contact-web {
    position: absolute;
    left: 40px;
    top: 604px;
    margin: 0;
    font-size: 44px;
    letter-spacing: 7.4px;
    color: var(--web-grey);
  }
  .contact-email {
    position: absolute;
    left: 60px;
    top: 651px;
    margin: 0;
    font-size: 45px;
    letter-spacing: 6.4px;
    color: var(--ink-navy);
  }
</style>
</head>
<body>
  <main class="appointment-card">
    <h1 class="card-heading">Next Appointment</h1>
    <div class="entry-field entry-date">
      <span class="field-label">Date</span>
      <span class="field-line"></span>
    </div>
    <div class="entry-field entry-time">
      <span class="field-label">Time</span>
      <span class="field-line"></span>
    </div>
    <p class="contact-web">www.pawluxemobilewash.com.au</p>
    <p class="contact-email">pawluxemobilewash@quillmail.com</p>
  </main>
</body>
</html>
```